Summit Builders Web Site / Business Cards

Construction Company that specializes in Water and Fire Damage, Residential ReModels, Landscaping and Building ADU (Accessory Dwelling Unit)

Growing and changing families often need additional space, and a remodeling project can often provide that. Adding a new area, or repurposing an existing one can satisfy this requirement.

Other times, homeowners want to update the look in their kitchen or bathroom with more than just a change of cabinetry or vanity doors and drawers. Whatever your needs are, Summit Builders has skilled workers who are bonded and insured, and ready to make your dreams and visions a reality.

Target Market(s)

Home Owners

Industry/Entity Type

Construction Company

Contact Information for Business Card

Center Logo with our information on the corners

Back side to be Logo Only
Contact Info
CSLB License # 4829516
info@summitbuildersca.example
www.summitbuildersca.example

Coding

Coded - Design and coding required

Number of Pages Required

5+ page

Font styles to use
Serif
Sans Serif

Requirements
Must have
• Using our Logo Colors
Home
About Us
Services
Projects / Portfolio
Contact Us
Nice to have
• Colors matching our Logo
Should not have
• Black because it doesnt match our logo

```html
<!DOCTYPE html>
<html lang="en">
<head>
<meta charset="utf-8">
<title>Summit Builders – Business Cards</title>
<link rel="stylesheet" href="https://fonts.googleapis.com/css2?family=Poppins:wght@500;600&display=swap">
<style>
  :root {
    --page-bg: #e4e4e6;
    --card-front: #e8631c;
    --card-light: #f6f6f4;
    --ink-dark: #3a3c40;
    --ink-light: #ffffff;
    --accent: #e8631c;
    --shadow: rgba(0, 0, 0, 0.2);
  }
  * { margin: 0; padding: 0; box-sizing: border-box; }
  html, body {
    width: 1200px;
    height: 900px;
    overflow: hidden;
    background: var(--page-bg);
    font-family: "Poppins", sans-serif;
  }
  .canvas {
    position: relative;
    width: 1200px;
    height: 900px;
    display: flex;
    align-items: center;
    justify-content: center;
    gap: 60px;
  }
  .card {
    position: relative;
    width: 520px;
    height: 298px;
    border-radius: 3px;
    box-shadow: 0 14px 30px var(--shadow);
    overflow: hidden;
  }
  .card--front { background: var(--card-front); }
  .card--back  { background: var(--card-light); }

  .brand {
    position: absolute;
    top: 50%;
    left: 50%;
    transform: translate(-50%, -50%);
    display: flex;
    align-items: center;
    gap: 12px;
    white-space: nowrap;
  }
  .brand__mark {
    width: 26px;
    height: 26px;
  }
  .card--front .brand__mark { background: var(--ink-light); }
  .card--back  .brand__mark { background: var(--accent); }
  .brand__name {
    font-weight: 600;
    font-size: 30px;
    letter-spacing: 0.04em;
    text-transform: uppercase;
  }
  .card--front .brand__name { color: var(--ink-light); }
  .card--back  .brand__name { color: var(--ink-dark); }

  .contact {
    position: absolute;
    font-weight: 600;
    font-size: 12.5px;
    color: var(--ink-dark);
    white-space: nowrap;
  }
  .contact--license {
    top: 50%;
    right: 18px;
    transform-origin: right top;
    transform: translate(0, -50%) rotate(90deg) translate(50%, -100%);
  }
  .contact--email {
    top: 50%;
    left: 18px;
    transform-origin: left top;
    transform: translate(0, -50%) rotate(-90deg) translate(-50%, 0);
  }
  .contact--web {
    bottom: 40px;
    left: 50%;
    transform: translateX(-50%);
  }
</style>
</head>
<body>
  <main class="canvas">
    <section class="card card--front" aria-label="Card front">
      <div class="brand">
        <span class="brand__mark"></span>
        <span class="brand__name">Summit Builders</span>
      </div>
    </section>

    <section class="card card--back" aria-label="Card back">
      <div class="brand">
        <span class="brand__mark"></span>
        <span class="brand__name">Summit Builders</span>
      </div>
      <p class="contact contact--license">CSLB License # 4829516</p>
      <p class="contact contact--email">info@summitbuildersca.example</p>
      <p class="contact contact--web">www.summitbuildersca.example</p>
    </section>
  </main>
</body>
</html>
```